Industry and Trade -may go complete production

Industrial and Corporate Clothing ecom and showcase web site
see supplier ref sites:
www.grellonworkgear.example.com.au
www.mickysprocket.example.com/,
www.Koradyn.example.com.au
Our logo is a roundal shaped gear cog with an elephant inside it.
Main Objective

Get people to contact us for industrial and corporate wear
order online or contact us for more details on products

Information in seconday pages inmportant and ISO standards etc.
Primary Points:

Must show that we are strong and solid.
Visual imagery is important.
We have many web sites in line and this is a start, see zanterfreight.example.com.au for one of ours.

We need a layout for the home page and internal pages. It's an ecomm retail site! Must sell the products AND our company.

Internal pages would be product description pages.

Each page must present an opportunity for them to contact us.
Updates

http://shop.qvx.example.com/siege-of-marrowfen-a-stonehelm-table-game/detail.php?p=481736&v=qvx_series_crown-of-ashes_games#tabs

has very good features 

Reason: Not Enough Responses. This will open up to a designer doing continuous designs for our company. We had lost our last in house designer and need a new innovative person to create genius.

Hi

This tender has been extended due to non response. 
This is our first look at the system as we had designers inder contract who have now left. There are may web sites etc to be done and this is more of a interview.

It is well worth responding. There are already 6 other projects in the pipline. But we want the best .
Barney ter Haust
Group COO Meridale Carriage Pty Ltd
Sydney Australia.

Target Market(s)

TARGET MARKET:
Tradesmen and Corporations and Government agencies
again see the above web sites they address the same markets
especially grellon.example.com.au

Industry/Entity Type

Industrial

Requirements
Must have
• Strength of company
supply and quality are important
ease of use, grellon.example.com.au can be used for good visual expression.
Nice to have
• extreme images and ease of use in navigation and contact.
look at imagery on grellon web site grellon.example.com.au
font useage: see http://money.quorvix.example.com.au/newsbusiness/wire/5193027/dalvane-signs-11b-grid-agreement for font size usage. clear clean to the point.
Should not have
• kitch

```html
<!DOCTYPE html>
<html lang="en">
<head>
<meta charset="utf-8">
<title>Ironmere Supply – Industrial and Corporate Clothing</title>
<link href="https://fonts.googleapis.com/css2?family=Black+Ops+One&family=Rubik+Dirt&family=Arimo:wght@400;700&display=swap" rel="stylesheet">
<style>
  :root{
    --page-dark:#262626;
    --page-darker:#161616;
    --gold:#f6d24c;
    --gold-deep:#e9b92a;
    --gold-pale:#fdf0b5;
    --panel:#fdf5cf;
    --ink:#5a5a5a;
    --ink-soft:#9a9a9a;
    --ink-light:#b8a870;
    --hero-yellow:#e9d04b;
    --hero-cream:#f3e9b0;
    --white:#ffffff;
    --plate-ink:#2f2f2f;
  }
  *{box-sizing:border-box;margin:0;padding:0}
  html,body{width:1200px;height:950px;overflow:hidden}
  body{
    position:relative;
    background:linear-gradient(180deg,#3a3a3a 0%,var(--page-dark) 40%,var(--page-darker) 100%);
    font-family:"Arimo",Arial,sans-serif;
    color:var(--ink);
  }
  .abs{position:absolute}

  /* top bar */
  .search{left:35px;top:26px;width:206px;height:22px;background:var(--white);border:1px solid #ccc}
  .search-btn{left:241px;top:26px;width:62px;height:22px;background:linear-gradient(#777,#333);color:var(--white);font:700 12px "Arimo",sans-serif;display:flex;align-items:center;justify-content:center}
  .login-label{left:895px;color:var(--white);font-size:13px}
  .login-field{left:985px;width:180px;height:19px;background:var(--white);border:1px solid #bbb}

  /* navigation */
  .nav{left:35px;top:58px;width:1130px;height:28px;background:linear-gradient(var(--gold),var(--gold-deep));border-radius:3px}
  .nav a{position:absolute;top:3px;font:19px "Black Ops One",sans-serif;color:#7a6a3a;text-decoration:none;letter-spacing:.5px}

  /* hero */
  .hero{left:35px;top:92px;width:1130px;height:316px;background:linear-gradient(135deg,#3b3b3b,#1e1e1e 60%,#2d2d2d)}
  .hero-title{font-family:"Rubik Dirt",sans-serif;color:var(--hero-yellow);line-height:1;white-space:nowrap}
  .hero-photo{left:598px;top:100px;width:567px;height:287px;border:5px solid var(--gold);border-radius:18px;background:linear-gradient(120deg,#4a4d4f,#a7acad 45%,#6d7173 70%,#c3c6c6)}
  .safety-gear{left:40px;top:272px;width:295px;height:136px;background:linear-gradient(160deg,#e9c93a,#c9a11c 55%,#9a9a9a)}
  .brand-plate{left:308px;top:188px;width:255px;height:150px;background:linear-gradient(160deg,#d2d2d2,#8d8d8d)}
  .brand{left:330px;top:246px;display:flex;align-items:center;gap:10px}
  .brand-mark{width:30px;height:30px;border-radius:50%;background:var(--plate-ink)}
  .brand-name{font:700 20px "Arimo",sans-serif;color:var(--plate-ink);white-space:nowrap}

  /* content */
  .content{left:35px;top:408px;width:1130px;height:498px;background:linear-gradient(180deg,#fff8d6 0%,var(--gold-pale) 12%,var(--gold) 70%,var(--gold-deep) 100%)}
  .panel{background:linear-gradient(180deg,var(--panel),#fbe79a);border-radius:3px 3px 3px 40px;box-shadow:0 2px 4px rgba(0,0,0,.15);padding:10px 10px}
  .panel-title{font:27px "Black Ops One",sans-serif;color:#6a6040;line-height:1}
  .small{font-size:10px;line-height:1.25;color:var(--ink-soft)}
  .date{font-size:13px;color:var(--ink-soft);margin-top:14px}
  .lead{font-size:15px;color:#8a8060}
  .more{display:block;text-align:right;font-size:10px;color:#8a8060;margin-top:14px}
  .product{background:linear-gradient(160deg,#3d4a66,#6f7a8e);border:3px solid var(--white)}

  .article-title{font:25px "Black Ops One",sans-serif;color:#8b8060;letter-spacing:1px}
  .article p{font-size:11.5px;line-height:1.33;color:var(--ink-light);margin-top:8px}

  .quote-btn{display:block;background:linear-gradient(#666,#222);color:var(--white);font:700 10px "Arimo",sans-serif;padding:3px 10px;border-radius:3px;margin-top:8px;line-height:1.2}
  .enews-title{text-align:center;font:700 15px "Arimo",sans-serif;color:#333}
  .email{display:flex;margin-top:6px}
  .email span{flex:1;background:var(--white);border:1px solid #aaa;font-size:14px;padding:1px 4px;color:#333}
  .email b{width:32px;background:linear-gradient(#b89a2a,#6e5a12);color:var(--gold);font-size:12px;text-align:center;line-height:20px}
  .social{display:flex;align-items:center;height:24px;margin-top:6px;background:linear-gradient(#fff5c8,#f7e08a);border:1px solid #e6cf7a;font-size:11px;color:#8a8060}
  .social i{width:16px;height:16px;margin:0 12px 0 6px}
  .social span{flex:1;text-align:center}
  .news-btn{display:block;margin-top:10px;text-align:center;background:linear-gradient(#777,#222);color:var(--white);font:700 12px "Arimo",sans-serif;padding:6px 0;border-radius:3px}

  /* footer */
  .footer{left:35px;top:906px;width:1130px;height:36px;background:#2b2b2b;color:var(--white);font-size:9px}
  .footer .copy{position:absolute;left:20px;top:13px}
  .footer .links{position:absolute;right:20px;top:13px;display:flex;gap:6px}
  .footer .links span+span{border-left:1px solid var(--white);padding-left:6px}
</style>
</head>
<body>
  <div class="abs search"></div>
  <div class="abs search-btn">Search</div>
  <div class="abs login-label" style="top:11px">Login</div>
  <div class="abs login-label" style="top:28px">User name</div>
  <div class="abs login-field" style="top:11px"></div>
  <div class="abs login-field" style="top:31px"></div>

  <nav class="abs nav">
    <a style="left:53px">Home</a>
    <a style="left:171px">Services</a>
    <a style="left:320px">Products</a>
    <a style="left:472px">About us</a>
    <a style="left:621px">FAQs</a>
    <a style="left:736px">Materials</a>
    <a style="left:898px">Contact</a>
    <a style="left:1035px">Shop</a>
  </nav>

  <header class="abs hero"></header>
  <div class="abs hero-title" style="left:50px;top:100px;font-size:46px">Industrial</div>
  <div class="abs hero-title" style="left:285px;top:143px;font-size:30px;color:var(--hero-cream)">and Corporate</div>
  <div class="abs hero-title" style="left:60px;top:185px;font-size:56px">clothing</div>
  <div class="abs safety-gear" role="img" aria-label="Yellow safety helmet and work gloves"></div>
  <div class="abs brand-plate" role="img" aria-label="Brushed metal name plate"></div>
  <div class="abs brand"><span class="brand-mark"></span><span class="brand-name">Ironmere Supply</span></div>
  <div class="abs hero-photo" role="img" aria-label="Close-up of steel machine gears"></div>

  <main class="abs content"></main>

  <section class="abs panel" style="left:49px;top:440px;width:220px;height:215px">
    <h2 class="panel-title">News</h2>
    <div class="date">12.06.2011</div>
    <div class="lead">Quisque vitae pede.</div>
    <p class="small" style="margin-top:8px">Quisque vitae pede. Nam et augue. Sed a elit. Ut vel massa. Suspendisse nibh pede, ultrices vitae,ultrices nec, mollis non nibh...</p>
    <span class="more">Learn more...</span>
  </section>

  <section class="abs panel" style="left:49px;top:674px;width:220px;height:224px">
    <h2 class="panel-title">Buy now</h2>
  </section>
  <div class="abs product" style="left:66px;top:720px;width:84px;height:82px" role="img" aria-label="Hi-vis workwear jacket"></div>
  <div class="abs product" style="left:168px;top:720px;width:84px;height:82px" role="img" aria-label="Navy work jacket"></div>
  <div class="abs product" style="left:168px;top:808px;width:84px;height:82px" role="img" aria-label="Grey work jacket"></div>

  <article class="abs article" style="left:299px;top:452px;width:616px">
    <h1 class="article-title">Quisque vitae pede.</h1>
    <p>Quisque vitae pede. Nam et augue. Sed a elit. Ut vel massa. Suspendisse nibh pede, ultrices vitae, ultrices nec, mollis non nibh.Quisque vitae pede. Nam et augue. Sed a elit. Ut vel massa. Suspendisse nibh pede, ultrices vitae,ultrices nec, mollis non nibh. Quisque vitae pede. Nam et augue. Sed a elit. Ut vel massa. Suspendisse nibh pede, ultrices vitae ultrices nec, mollis non nibh. Quisque vitae pede. Nam et augue. Sed a elit. Ut vel massa. Suspendisse nibh pede, ultrices vitae ultrices nec, mollis non nibh... Quisque vitae pede. Nam et augue. Sed a elit. Ut vel massa. Suspendisse nibh pede, ultrices vitae ultrices nec, mollis non nibh... Suspendisse nibh pede, ultrices vitae ultrices nec, mollis non nibh...</p>
    <h1 class="article-title" style="margin-top:14px">Quisque vitae pede.</h1>
    <p>Quisque vitae pede. Nam et augue. Sed a elit. Ut vel massa. Suspendisse nibh pede, ultrices vitae, ultrices nec, mollis non nibh.Quisque vitae pede. Nam et augue. Sed a elit. Ut vel massa. Suspendisse nibh pede, ultrices vitae,ultrices nec, mollis non nibh. Quisque vitae pede. Nam et augue. Sed a elit. Ut vel massa. Suspendisse nibh pede, ultrices vitae ultrices nec, mollis non nibh. Quisque vitae pede. Nam et augue. Sed a elit. Ut vel massa. Suspendisse nibh pede, ultrices vitae ultrices nec, mollis non nibh... Quisque vitae pede. Nam et augue. Sed a elit. Ut vel massa. Suspendisse nibh pede, ultrices vitae ultrices nec, mollis non nibh... Suspendisse nibh pede, ultrices vitae ultrices nec, mollis non nibh...</p>
    <p style="margin-top:12px">Suspendisse nibh pede, ultrices vitae ultrices nec, mollis non nibh... Suspendisse nibh pede, ultrices vitae ultrices nec, mollis non nibh...</p>
  </article>

  <section class="abs panel" style="left:933px;top:440px;width:220px;height:211px">
    <h2 class="panel-title" style="font-size:25px">Request<br>a Quote</h2>
    <div class="lead" style="font-size:13px;margin-top:4px">Quisque vitae pede.</div>
    <p class="small">Quisque vitae pede. Nam et augue. Sed a elit. Ut vel massa. Suspendisse nibh pede, ultrices vitae,ultrices nec, mollis non nibh...</p>
    <span class="quote-btn">Contact us for a no obligation free quote.</span>
  </section>

  <section class="abs panel" style="left:933px;top:674px;width:220px;height:224px">
    <div class="enews-title">eNews sign up</div>
    <div class="email"><span>Your email</span><b>GO</b></div>
    <div class="social"><i style="background:#3b5b99"></i><span>like us on Friendvine</span></div>
    <div class="social"><i style="background:#35a8dc"></i><span>follow us on Chirpline</span></div>
    <div class="social"><i style="background:#f28a1e"></i><span>subscribe to rss feed</span></div>
    <span class="news-btn">eNews Letter</span>
  </section>

  <footer class="abs footer">
    <span class="copy">Copyright ©2011 All rights reserved</span>
    <span class="links"><span>Contact us</span><span>Terms and Conditions</span><span>Site map</span></span>
  </footer>
</body>
</html>
```